Bellmoor Glassware Brand Design

Logo Design Brief

Bellmoor Glassware is a startup premium drinkware company launching its first product - a premium grade 24oz Copa de Balon Gin Glass.

We are looking for branding design to produce our logo and the label for our first product; a premium 24oz Copa de Balon Gin Glass.

Design Brief for logo:

• Premium brand
• Modern, elegant and sleek design
• Not busy
• Logo does not have to include reference to drinkware

Label Design Brief:

A label design for our packaging - The packaging is tubular and will house 2 gin glasses for retail sale. The label will be stuck on the front of the tube and will need to excite people about the purchase they have just made with Bellmoor Glassware.
The label design needs to incorporate the logo and reflect our premium brand image.

• The label size is 460mm x 150mm

• Label must have modern and sleek look and must not look busy.

• The label will need to work well in both multicolour and single colour print.

• Please see attached Barcode, this will need to be incorporated into the label. Barcode will need to be 300dpi or higher and 381mm x 254mm to be scannable on the packaging.

• Please see attached pictures of the tubular packaging the label is going on to

Please also see attached 3 images of the glasses being sold - This is for reference only.

Design period has been extended for 5 Days, please ensure both a logo and corresponding packaging design is submitted. Thank you Added Wednesday, October 4, 2017

Target Market(s)

Gin Drinkers - Premium - Male and Female - All ages above 18

Industry/Entity Type

It Company

Logo Text

Bellmoor

Font styles to use
Serif
Sans Serif

Colors

Designer to choose colors to be used in the design.

Requirements
Must have
• Sleek modern design. Logo and Label must be submitted on this project.
Should not have
• Do not make this a busy logo or label

```html
<!DOCTYPE html>
<html lang="en">
<head>
<meta charset="utf-8">
<title>Bellmoor Glassware – Gin Glass Labels</title>
<link rel="stylesheet" href="https://fonts.googleapis.com/css2?family=Montserrat:wght@300;400;500&display=swap">
<style>
  :root {
    --backdrop: #5c5c5c;
    --label-light: #f3f3f3;
    --label-dark: #242021;
    --copper: #9b6a4d;
    --copper-soft: #a8795c;
  }
  * { margin: 0; padding: 0; box-sizing: border-box; }
  html, body {
    width: 1121px;
    height: 1200px;
    overflow: hidden;
    background: var(--backdrop);
    font-family: "Montserrat", Arial, sans-serif;
  }
  .label-set {
    position: absolute;
    top: 100px;
    left: 120px;
    display: flex;
    gap: 81px;
  }
  .label {
    position: relative;
    width: 400px;
    height: 1000px;
    color: var(--copper);
  }
  .label--light { background: var(--label-light); }
  .label--dark { background: var(--label-dark); color: var(--copper-soft); }

  .brand-mark {
    position: absolute;
    top: 42px;
    left: 50%;
    width: 130px;
    height: 130px;
    margin-left: -65px;
    border: 3px solid currentColor;
    border-radius: 50%;
  }
  .brand-name {
    position: absolute;
    top: 198px;
    width: 100%;
    text-align: center;
    font-weight: 300;
    line-height: 1;
  }
  .brand-name__main {
    display: block;
    font-size: 50px;
    letter-spacing: 3px;
    padding-left: 3px;
  }
  .brand-name__sub {
    display: block;
    margin-top: 10px;
    font-size: 17px;
    letter-spacing: 8.5px;
    padding-left: 8.5px;
  }
  .product-name {
    position: absolute;
    top: 333px;
    left: 50%;
    height: 410px;
    margin-left: -12px;
    writing-mode: vertical-rl;
    transform: rotate(180deg);
    font-size: 19px;
    font-weight: 400;
    letter-spacing: 6.3px;
    text-align: center;
    white-space: nowrap;
  }
  .capacity-glass {
    position: absolute;
    top: 776px;
    left: 50%;
    width: 80px;
    height: 142px;
    margin-left: -40px;
  }
  .base-rule {
    position: absolute;
    left: 0;
    width: 100%;
    background: currentColor;
  }
  .base-rule--thick { top: 915px; height: 4px; }
  .base-rule--thin { top: 932px; height: 1.5px; }
  .variant-name {
    position: absolute;
    top: 954px;
    width: 100%;
    text-align: center;
    font-size: 21px;
    font-weight: 500;
    letter-spacing: 6px;
    padding-left: 6px;
  }
</style>
</head>
<body>
  <main class="label-set">
    <section class="label label--light">
      <div class="brand-mark"></div>
      <h1 class="brand-name">
        <span class="brand-name__main">BELLMOOR</span>
        <span class="brand-name__sub">GLASSWARE</span>
      </h1>
      <p class="product-name">COPA DE BALÓN GIN GLASS</p>
      <svg class="capacity-glass" viewBox="0 0 80 142" aria-label="21.75 oz glass">
        <path d="M4 2 H76 C82 40 70 68 46 74 V118 C46 128 56 134 72 139 H8 C24 134 34 128 34 118 V74 C10 68 -2 40 4 2 Z" fill="currentColor"/>
        <text x="40" y="30" text-anchor="middle" font-family="Montserrat, sans-serif" font-size="20" font-weight="500" fill="var(--label-light)">21.75</text>
        <text x="40" y="52" text-anchor="middle" font-family="Montserrat, sans-serif" font-size="16" letter-spacing="4" fill="var(--label-light)">OZ</text>
      </svg>
      <div class="base-rule base-rule--thick"></div>
      <div class="base-rule base-rule--thin"></div>
      <p class="variant-name">SIERRA</p>
    </section>

    <section class="label label--dark">
      <div class="brand-mark"></div>
      <h1 class="brand-name">
        <span class="brand-name__main">BELLMOOR</span>
        <span class="brand-name__sub">GLASSWARE</span>
      </h1>
      <p class="product-name">COPA DE BALÓN GIN GLASS</p>
      <svg class="capacity-glass" viewBox="0 0 80 142" aria-label="24 oz glass">
        <path d="M4 2 H76 C82 40 70 68 46 74 V118 C46 128 56 134 72 139 H8 C24 134 34 128 34 118 V74 C10 68 -2 40 4 2 Z" fill="currentColor"/>
        <text x="40" y="30" text-anchor="middle" font-family="Montserrat, sans-serif" font-size="20" font-weight="500" letter-spacing="4" fill="var(--label-dark)">24</text>
        <text x="40" y="52" text-anchor="middle" font-family="Montserrat, sans-serif" font-size="16" letter-spacing="4" fill="var(--label-dark)">OZ</text>
      </svg>
      <div class="base-rule base-rule--thick"></div>
      <div class="base-rule base-rule--thin"></div>
      <p class="variant-name">LANTERN</p>
    </section>
  </main>
</body>
</html>
```